Illustration Design Project

I have an existing illustration I have written up, I need it professionally redone, perhaps as an infographic or new design from the current layout.

Pls plan for a few edits and revisions.

I will need it large enough to be made into a wall poster size.

```html
<!DOCTYPE html>
<html lang="en">
<head>
<meta charset="utf-8">
<title>Being Accountable vs. Being a Victim</title>
<link rel="stylesheet" href="https://fonts.googleapis.com/css2?family=Arimo:wght@400;700&family=Shadows+Into+Light&display=swap">
<style>
  :root {
    --paper: #dcdcd8;
    --ink: #111111;
    --chalk: #ffffff;
    --dot: #1b1bb8;
    --quote: #2f6fe0;
    --victim-label: #6a6ae6;
    --head-up: #56698a;
    --head-mid: #3b4160;
    --head-down: #9c6b6b;
  }
  html, body { margin: 0; padding: 0; overflow: hidden; }
  body { width: 800px; height: 1200px; background: var(--paper); }
  .poster {
    position: relative; width: 800px; height: 1200px; overflow: hidden;
    background: var(--paper);
    font-family: "Arimo", Arial, sans-serif;
  }
  .chalk { position: absolute; inset: 0; width: 800px; height: 1200px; }
  .subtitle {
    position: absolute; top: 44px; left: 0; width: 790px; text-align: center;
    font-size: 23px; color: var(--ink); margin: 0; font-weight: 400;
  }
  .heading {
    position: absolute; left: 0; width: 790px; text-align: center; margin: 0;
    font-size: 40px; font-weight: 700; letter-spacing: 1px; line-height: 1;
  }
  .heading--accountable { top: 88px; color: var(--head-up); }
  .heading--life { top: 632px; color: var(--head-mid); }
  .heading--victim { top: 1128px; color: var(--head-down); }
  .step { position: absolute; left: 0; width: 800px; }
  .step__label {
    position: absolute; right: 446px; top: 0; transform: translateY(-50%);
    text-align: right; font-size: 36px; font-weight: 700; line-height: 48px;
    white-space: nowrap;
  }
  .step__label--ahead { color: var(--ink); }
  .step__label--behind { color: var(--victim-label); }
  .step__num {
    position: absolute; left: 388px; top: -13px; width: 26px; height: 26px;
    border-radius: 50%; background: var(--dot); color: #fff;
    font-size: 18px; font-weight: 700; text-align: center; line-height: 26px;
  }
  .step__quote {
    position: absolute; left: 440px; top: 0; transform: translateY(-50%);
    font-family: "Shadows Into Light", cursive; color: var(--quote);
    font-size: 31px; line-height: 40px; white-space: nowrap; letter-spacing: 1px;
  }
</style>
</head>
<body>
<main class="poster">
  <svg class="chalk" viewBox="0 0 800 1200" aria-hidden="true" fill="none" stroke="var(--chalk)" stroke-width="5" stroke-linecap="round" stroke-linejoin="round">
    <line x1="400" y1="140" x2="400" y2="585"/>
    <polyline points="390,152 400,136 410,152"/>
    <line x1="400" y1="690" x2="400" y2="1130"/>
    <polyline points="390,1118 400,1134 410,1118"/>
    <path d="M228 108 C 60 140, 10 300, 22 420 C 34 540, 120 610, 208 636"/>
    <polyline points="186,618 210,637 184,650"/>
    <path d="M492 1140 C 640 1120, 760 1000, 748 860 C 736 740, 660 680, 570 658"/>
    <polyline points="590,645 566,657 588,672"/>
  </svg>

  <h2 class="subtitle">Being Accountable vs. Being a Victim</h2>
  <h1 class="heading heading--accountable">ACCOUNTABLE</h1>

  <div class="step" style="top:196px">
    <div class="step__label step__label--ahead">Gets on with it</div>
    <div class="step__num">5</div>
    <div class="step__quote">"O.K., let's do it!"</div>
  </div>
  <div class="step" style="top:262px">
    <div class="step__label step__label--ahead">Finds solution</div>
    <div class="step__num">4</div>
    <div class="step__quote">"What can I do?"</div>
  </div>
  <div class="step" style="top:338px">
    <div class="step__label step__label--ahead">Owns it</div>
    <div class="step__num">3</div>
    <div class="step__quote" style="top:12px">"If it's to be, it's<br>up to me!"</div>
  </div>
  <div class="step" style="top:406px">
    <div class="step__label step__label--ahead" style="top:22px;text-align:right">Acknowledges<br>reality</div>
    <div class="step__num">2</div>
    <div class="step__quote" style="top:18px">"This is the way<br>&nbsp;&nbsp;it is."</div>
  </div>
  <div class="step" style="top:512px">
    <div class="step__label step__label--ahead" style="top:24px">Seeks<br>reality</div>
    <div class="step__num">1</div>
    <div class="step__quote">"What's happening?"</div>
  </div>

  <h1 class="heading heading--life">LIFE HAPPENS</h1>

  <div class="step" style="top:726px">
    <div class="step__label step__label--behind">Avoids reality</div>
    <div class="step__num">1</div>
    <div class="step__quote">"Asks no questions."</div>
  </div>
  <div class="step" style="top:812px">
    <div class="step__label step__label--behind">Fights reality</div>
    <div class="step__num">2</div>
    <div class="step__quote" style="top:8px">"That's not how<br>&nbsp;I see it."</div>
  </div>
  <div class="step" style="top:882px">
    <div class="step__label step__label--behind">Blames</div>
    <div class="step__num">3</div>
    <div class="step__quote" style="top:18px">"If everyone would<br>just do their job!"</div>
  </div>
  <div class="step" style="top:952px">
    <div class="step__label step__label--behind">Personal excuses</div>
    <div class="step__num">4</div>
    <div class="step__quote" style="top:4px">"Is not my job."</div>
  </div>
  <div class="step" style="top:1046px">
    <div class="step__label step__label--behind">Waits, hoppes</div>
    <div class="step__num">5</div>
    <div class="step__quote" style="top:16px">"If it was meant<br>to be, it'll happen!"</div>
  </div>

  <h1 class="heading heading--victim">VICTIM</h1>
</main>
</body>
</html>
```